8-page brochure for laboratory equipment in the beverage can industry

We are a small company in the quality inspection and testing industry for beverage and food cans and are in need of a product brochure for one of our key products.The brochure should comprise of 8-pages. We will need both a print-ready format (which we would like to print on 2 double-sided A3 pages, then fold them), as well as an electronic version of the brochure (PDF). We also need to be able to make modifications to it, so we will need the open design file.We have corporate colors and fonts that will have to be used, which we will provide you with.The structure and content are defined, but we need some creative thinking to make it look great!

Target Market(s)

Beverage fillers

Font styles to use
Other font styles liked:
• Nexa Bold, Gotham Book, Calibri

Requirements
Must have
• Must be informative and look appealing.
• Must use the content from the Word document provided (better quality images will be provided if needed).
• Must use the company's corporate colors and fonts.
• Colors:
• Green: CMYK 99, 21, 86, 7
• Dark Grey: CMYK 67, 62, 58, 45
• Light Grey: CMYK 45, 36, 35, 1

```html
<!DOCTYPE html>
<html lang="en">
<head>
<meta charset="utf-8">
<title>Norvale Seamtech – Seam Inspection Systems Brochure</title>
<link rel="stylesheet" href="https://fonts.googleapis.com/css2?family=Open+Sans:ital,wght@0,300;0,400;0,600;0,700;0,800;1,700;1,800&display=swap">
<style>
:root{
  --green:#00845a;
  --plum:#3a2b2e;
  --grey-dark:#4a4542;
  --grey-light:#8f9396;
  --paper:#ffffff;
  --stage:#e4e4e4;
  --line:#d9dcdc;
  --text:#4b4b4b;
}
*{box-sizing:border-box;margin:0;padding:0}
html,body{width:1200px;height:4808px;overflow:hidden}
body{background:var(--stage);font-family:"Open Sans",Arial,sans-serif;color:var(--text)}
.sheet{position:relative;height:961.6px;display:flex;align-items:center;justify-content:center;border-bottom:2px solid #f2f2f2}
.page{position:relative;width:520px;height:736px;background:var(--paper);overflow:hidden;box-shadow:0 6px 18px rgba(0,0,0,.12)}
.spread{display:flex;box-shadow:0 8px 22px rgba(0,0,0,.14)}
.spread .page{box-shadow:none}
.spread .page+.page{border-left:1px solid #e8e8e8}
.ph{position:absolute;border-radius:2px}
.small{font-size:8px;line-height:1.5;color:var(--text)}
.small p{margin-bottom:5px}
.q{font-weight:700;font-size:8.5px;color:var(--grey-dark);margin-top:6px}
.abs{position:absolute}

/* cover */
.brand{position:absolute;left:34px;top:36px;display:flex;align-items:center;gap:7px;font-weight:800;font-size:17px;color:var(--grey-dark);letter-spacing:.5px}
.brand i{width:12px;height:12px;background:var(--green);display:block}
.brand-tag{position:absolute;left:53px;top:60px;font-size:7px;color:var(--grey-light)}
.cover-city{left:0;top:90px;width:520px;height:220px;background:linear-gradient(180deg,#fff 0%,#e7e9e9 45%,#f4f5f5 100%)}
.cover-title{position:absolute;right:36px;top:100px;text-align:right}
.cover-title .thin{font-weight:300;font-size:30px;color:var(--grey-light);letter-spacing:1px}
.cover-title .bold{font-weight:800;font-size:32px;color:var(--green);line-height:1.02}
.prod-box{position:absolute;background:var(--plum);color:#fff;font-weight:600;font-size:22px;display:flex;align-items:center;justify-content:center;text-align:center;line-height:1.1}
.cover-band{position:absolute;left:0;bottom:0;width:520px;height:142px;background:var(--green);display:flex;align-items:flex-end;justify-content:center;padding-bottom:30px;color:#fff;font-size:13px}

/* headings */
.h-green{font-weight:800;font-style:italic;color:#fff}
.h-text{font-weight:800;font-style:italic;color:var(--green)}
.bar-grey{position:absolute;background:#e6e7e7;color:var(--grey-dark);font-weight:700;font-style:italic;font-size:13px;padding:5px 12px}
.benefit b{display:block;font-size:8.5px;color:var(--grey-dark);margin-top:7px}
.caption{position:absolute;font-size:7.5px;font-weight:700;color:var(--grey-dark)}
.table{position:absolute;background:var(--green);padding:30px 14px 14px}
.table h4{position:absolute;top:9px;left:0;right:0;text-align:center;color:#fff;font-size:10px;letter-spacing:1px}
.table table{width:100%;border-collapse:collapse;background:#fff;font-size:7.5px}
.table td{border-bottom:1px solid var(--line);padding:4px 6px}
.table td:first-child{font-weight:700;color:var(--grey-dark);width:36%;background:#f3f4f4}
.col-head{background:var(--green);color:#fff;font-weight:700;font-size:9px;padding:6px 8px}
.col-body{padding:6px 2px}
</style>
</head>
<body>

<!-- Cover -->
<section class="sheet">
  <article class="page cover">
    <div class="ph cover-city" role="img" aria-label="Faded industrial city skyline"></div>
    <div class="brand"><i></i>NORVALE SEAMTECH</div>
    <div class="brand-tag">Quality inspection for cans</div>
    <div class="cover-title">
      <div class="thin">NON-DESTRUCTIVE</div>
      <div class="bold">SEAM INSPECTION<br>SYSTEMS</div>
    </div>
    <div class="prod-box" style="left:300px;top:220px;width:190px;height:90px">SEAMview<br>RX 3</div>
    <div class="ph" role="img" aria-label="Bench-top seam inspection unit" style="left:300px;top:320px;width:190px;height:170px;background:linear-gradient(160deg,#e9e9e7,#c8c9c6)"></div>
    <div class="ph" role="img" aria-label="Automated inline X-ray seam inspection cabinet" style="left:30px;top:300px;width:260px;height:170px;background:linear-gradient(160deg,#efeeea,#cfcec8)"></div>
    <div class="prod-box" style="left:30px;top:480px;width:260px;height:110px">AUTO RX</div>
    <div class="cover-band">www.norvale-seamtech.example</div>
  </article>
</section>

<!-- Back cover: FAQ -->
<section class="sheet">
  <article class="page">
    <svg style="position:absolute;left:0;top:0" width="520" height="130" aria-hidden="true">
      <path d="M120 0H520V130Q400 60 120 40Z" fill="var(--green)"/>
    </svg>
    <div class="h-green abs" style="right:30px;top:26px;font-size:24px">Frequently asked questions</div>
    <div class="small abs" style="left:30px;top:84px;width:220px">
      <div class="q">• Why is X-ray better than cutting the seam?</div><p>It checks the whole seam without damage, so the same can stays intact and can be tested again later.</p>
      <div class="q">• How long does one measurement take?</div><p>A full seam check takes well under a minute per can, including loading and the final report.</p>
      <div class="q">• Which seam values are measured?</div><p>Body hook, cover hook, overlap, seam thickness, countersink and wrinkle rating in one run.</p>
      <div class="q">• Can results be exported?</div><p>Yes, all data flows into the quality software and can be saved in common file formats.</p>
      <div class="q">• What can sizes are supported?</div><p>Most standard beverage and food can diameters and heights are covered by quick tooling.</p>
      <div class="q">• Is the system safe to run?</div><p>The cabinet is fully shielded and meets the radiation rules that apply in each region.</p>
      <div class="q">• Does it need a special room?</div><p>No, it fits in a normal lab next to the line with standard power and network.</p>
      <div class="q">• How are the values checked?</div><p>Each unit is set up with reference cans and checked at regular service visits.</p>
    </div>
    <div class="small abs" style="left:270px;top:140px;width:220px">
      <div class="q">• Who operates the system?</div><p>Any trained lab staff member can run it after a short session on site.</p>
      <div class="q">• Is training included?</div><p>On-site setup and operator training come with every unit we deliver.</p>
      <div class="q">• How is service handled?</div><p>Local partners and remote support cover all regions with fast response times.</p>
      <div class="q">• Can it match current methods?</div><p>Results correlate closely with manual teardown values used in most plants.</p>
      <div class="q">• Can limits be set per can type?</div><p>Yes, each can type keeps its own limits, alarms and report layout.</p>
      <div class="q">• How easy is it to set up?</div><p>Setup needs only power, a network point and a stable bench or floor space.</p>
      <div class="q">• Is an upgrade path available?</div><p>Bench units can later be linked to the automatic version and plant software.</p>
    </div>
    <div class="abs" style="left:0;bottom:0;width:520px;height:150px;background:var(--green);color:#fff;padding:18px 24px;font-size:7.5px;line-height:1.5">
      <div style="display:grid;grid-template-columns:repeat(4,1fr);gap:10px">
        <div><b>GERMANY</b><br>Tel: +49 000 0000<br>de@norvale-seamtech.example</div>
        <div><b>UNITED STATES</b><br>Tel: +1 000 000 0000<br>us@norvale-seamtech.example</div>
        <div><b>MEXICO</b><br>Tel: +52 00 0000 0000<br>mx@norvale-seamtech.example</div>
        <div><b>CHINA</b><br>Tel: +86 000 0000<br>cn@norvale-seamtech.example</div>
      </div>
      <div style="text-align:center;font-size:13px;margin-top:34px">www.norvale-seamtech.example</div>
    </div>
  </article>
</section>

<!-- Spread: benefits / how it works -->
<section class="sheet">
  <div class="spread">
    <article class="page">
      <svg style="position:absolute;left:0;top:0" width="520" height="736" aria-hidden="true">
        <path d="M0 0H300Q260 60 0 70Z" fill="var(--green)"/>
        <path d="M0 450L250 736H0Z" fill="var(--green)"/>
      </svg>
      <div class="h-green abs" style="left:24px;top:14px;font-size:19px;line-height:1.1">Benefits of<br>RX technology</div>
      <div class="small benefit abs" style="left:24px;top:80px;width:225px">
        <b>SAVES TIME</b>No manual cutting or grinding, the full seam is measured in one quick pass.
        <b>SAVES MONEY</b>Fewer scrapped cans, less lab labour and lower cost per test.
        <b>INCREASED ACCURACY</b>Repeatable values that do not depend on the operator.
        <b>100% SEAM SAFETY</b>The whole seam is seen all the way round, not only a slice.
        <b>LESS SPILLAGE</b>Filled cans stay closed, so no product is lost during tests.
        <b>INCREASED SAFETY</b>No sharp tools or cut metal edges at the lab bench.
        <b>CERTIFICATION</b>Traceable records for customer audits and approvals.
        <b>FULLY AUTOMATIC VERSION AVAILABLE</b>Inline sampling with no operator needed.
      </div>
      <div class="h-text abs" style="left:280px;top:86px;font-size:14px;width:210px;line-height:1.2">What do we mean by RX seam scanning technology?</div>
      <div class="small abs" style="left:280px;top:140px;width:210px"><p>The seam is imaged by X-ray at many points, giving true cross-sections without opening the can.</p></div>
      <div class="ph" role="img" aria-label="Can seam cross-section scan" style="left:290px;top:190px;width:200px;height:100px;background:linear-gradient(135deg,#2f3640,#8a93a0)"></div>
      <div class="caption" style="left:290px;top:296px">Seam cross-section view</div>
      <div class="ph" role="img" aria-label="Seam thickness X-ray image" style="left:290px;top:312px;width:200px;height:90px;background:linear-gradient(135deg,#111,#6a6a6a)"></div>
      <div class="caption" style="left:290px;top:408px">X-ray projection (radial)</div>
      <div class="ph" role="img" aria-label="Colour-coded seam measurement strips" style="left:270px;top:430px;width:220px;height:120px;background:linear-gradient(90deg,#c9d7e6,#e9c9b8)"></div>
      <div class="caption" style="left:270px;top:556px">Measured values around the seam</div>
      <div class="ph" role="img" aria-label="Seam profile scan" style="left:290px;top:580px;width:200px;height:110px;background:linear-gradient(135deg,#263046,#7e8ba3)"></div>
      <div class="caption" style="left:290px;top:696px">Seam profile compared to limits</div>
    </article>
    <article class="page">
      <svg style="position:absolute;left:0;top:0" width="520" height="120" aria-hidden="true">
        <path d="M0 60Q120 10 520 0V70Q200 60 0 120Z" fill="var(--green)"/>
      </svg>
      <div class="h-green abs" style="left:30px;top:40px;font-size:17px;line-height:1.1">How does X-ray seam<br>measurement work?</div>
      <div class="small abs" style="left:30px;top:130px;width:235px">
        <p>The can is rotated in front of an X-ray source while a detector records the seam from many angles. Software then builds clear cross-sections of the seam at every point around the can.</p>
        <p>All key values are measured automatically and compared with the limits set for each can type. Out-of-limit points are marked in colour on screen.</p>
        <p>Results are stored with date, line and shift, ready for reports and audits.</p>
      </div>
      <div class="ph" role="img" aria-label="Technical diagram of X-ray source, can and detector" style="left:280px;top:130px;width:210px;height:150px;background:linear-gradient(180deg,#f6f6f6,#e3e5e5);border:1px solid var(--line)"></div>
      <div class="bar-grey" style="left:30px;top:300px;width:460px">Wrinkle rating with X-ray</div>
      <div class="small abs" style="left:30px;top:335px;width:460px">
        <p>• Wrinkles are rated on the full seam length, not on a single cut sample.</p>
        <p>• Images show each wrinkle in colour by severity for quick review.</p>
        <p>• Ratings follow the usual industry scale for easy comparison with past data.</p>
      </div>
      <div class="ph" role="img" aria-label="Wrinkle rating scan strips" style="left:30px;top:410px;width:460px;height:130px;background:linear-gradient(180deg,#dfe6ee,#c9d4e0)"></div>
      <div class="ph" role="img" aria-label="Opened seam with wrinkle marks" style="left:30px;top:560px;width:220px;height:140px;background:linear-gradient(135deg,#8c8f6e,#c9c6a4)"></div>
      <div class="ph" role="img" aria-label="Colour-coded wrinkle map" style="left:270px;top:560px;width:220px;height:140px;background:linear-gradient(135deg,#d7c6c6,#c4cbd9)"></div>
    </article>
  </div>
</section>

<!-- Spread: products -->
<section class="sheet">
  <div class="spread">
    <article class="page">
      <div class="h-text abs" style="left:30px;top:26px;font-size:22px;line-height:1">OUR<br>PRODUCTS</div>
      <div class="ph" role="img" aria-label="SEAMview RX 3 bench unit" style="left:180px;top:26px;width:200px;height:110px;background:linear-gradient(160deg,#efefec,#c9cac6)"></div>
      <div class="abs" style="left:30px;top:148px;font-weight:800;font-size:11px;color:var(--green)">SEAMVIEW RX 3</div>
      <div class="small abs" style="left:30px;top:166px;width:300px">
        <p>A compact lab system for full seam checks on beverage and food cans. It measures all key seam values in one run and stores every result with its images.</p>
        <p>Built for daily use by line and lab staff, with a simple touch screen, guided steps and fast change between can sizes.</p>
        <p>Works with filled or empty cans and links to the plant quality software.</p>
      </div>
      <div class="abs" style="left:350px;top:148px;font-size:8px;font-weight:700;color:var(--grey-dark)">FEATURES</div>
      <div class="small abs" style="left:350px;top:164px;width:150px">
        <p>• Full 360° seam view</p><p>• Quick can change</p><p>• Touch screen control</p><p>• Colour limit marks</p><p>• Data export</p><p>• Shielded cabinet</p>
      </div>
      <div class="table" style="left:0;top:330px;width:520px;height:406px">
        <h4>TECHNICAL DETAILS</h4>
        <table>
          <tr><td>Can diameter</td><td>50 – 100 mm</td></tr>
          <tr><td>Can height</td><td>up to 220 mm</td></tr>
          <tr><td>Measured values</td><td>Body hook, cover hook, overlap, thickness</td></tr>
          <tr><td>Wrinkle rating</td><td>Full seam length, colour coded</td></tr>
          <tr><td>Cycle time</td><td>under 60 s per can</td></tr>
          <tr><td>Accuracy</td><td>± 0.01 mm</td></tr>
          <tr><td>Power supply</td><td>230 V / 50 Hz</td></tr>
          <tr><td>Dimensions</td><td>1400 × 800 × 1300 mm</td></tr>
          <tr><td>Weight</td><td>approx. 600 kg</td></tr>
          <tr><td>Radiation safety</td><td>Fully shielded cabinet</td></tr>
          <tr><td>Software</td><td>ClearSight QC</td></tr>
          <tr><td>Options</td><td>Barcode input, network link</td></tr>
        </table>
      </div>
    </article>
    <article class="page">
      <div class="ph" role="img" aria-label="AUTO RX automated inspection unit" style="left:30px;top:60px;width:200px;height:150px;background:linear-gradient(160deg,#efefec,#c4c5c1)"></div>
      <div class="abs" style="left:30px;top:225px;font-weight:800;font-size:11px;color:var(--green)">AUTO RX</div>
      <div class="small abs" style="left:30px;top:245px;width:260px">
        <p>The fully automatic version takes cans from the line, checks the seam and returns results with no operator needed.</p>
        <p>Ideal for high-speed fillers that want every line sampled around the clock, with alarms sent straight to the line team.</p>
      </div>
      <div class="abs" style="left:310px;top:60px;width:185px;height:290px;border:1px solid var(--line);padding:10px">
        <div style="font-size:8px;font-weight:700;color:var(--grey-dark);margin-bottom:6px">FEATURES</div>
        <div class="small"><p>• Inline sampling from the line</p><p>• Multi-line input</p><p>• Automatic reports per shift</p><p>• Alarm on limits</p><p>• Remote access</p><p>• Low upkeep</p><p>• Same values as bench unit</p><p>• Full data history</p></div>
      </div>
      <div class="table" style="left:0;top:390px;width:520px;height:346px">
        <h4>TECHNICAL DETAILS</h4>
        <table>
          <tr><td>Can diameter</td><td>50 – 100 mm</td></tr>
          <tr><td>Sample lines</td><td>up to 8</td></tr>
          <tr><td>Cycle time</td><td>under 90 s per can</td></tr>
          <tr><td>Measured values</td><td>Hooks, overlap, thickness, wrinkle</td></tr>
          <tr><td>Power supply</td><td>400 V / 50 Hz</td></tr>
          <tr><td>Dimensions</td><td>2200 × 1200 × 1900 mm</td></tr>
          <tr><td>Weight</td><td>approx. 1100 kg</td></tr>
          <tr><td>Software</td><td>ClearSight QC</td></tr>
        </table>
      </div>
    </article>
  </div>
</section>

<!-- Spread: software / solutions -->
<section class="sheet">
  <div class="spread">
    <article class="page">
      <svg style="position:absolute;left:0;top:0" width="520" height="160" aria-hidden="true">
        <path d="M0 0H190Q120 70 0 150Z" fill="var(--green)"/>
      </svg>
      <div class="abs" style="left:210px;top:34px;font-weight:800;font-size:20px;color:var(--grey-dark)">ClearSight QC</div>
      <div class="ph" role="img" aria-label="Quality software screenshot with charts and seam images" style="left:210px;top:72px;width:290px;height:200px;background:linear-gradient(180deg,#f4f6f6,#dde2e2);border:1px solid var(--line)"></div>
      <div class="h-text abs" style="left:30px;top:190px;font-size:18px">ClearSight QC™</div>
      <div class="abs" style="left:30px;top:216px;font-size:8px;color:var(--grey-light);width:170px">Quality data collection and analysis software</div>
      <div class="small abs" style="left:30px;top:290px;width:460px"><p>One tool collects seam results from every system, shows trends by line and shift, and flags cans that drift toward their limits before problems reach the customer.</p></div>
      <div class="abs" style="left:30px;top:340px;width:460px;display:grid;grid-template-columns:repeat(3,1fr);gap:10px">
        <div><div class="col-head">ClearSight QC™ Light</div><div class="small col-body"><p>Basic data capture and reports for one lab.</p><p>• Single system link</p><p>• Shift reports</p><p>• Limit alarms</p></div></div>
        <div><div class="col-head">ClearSight QC™ Plant</div><div class="small col-body"><p>Links all lines and labs in one site.</p><p>• All systems in one view</p><p>• Trend charts</p><p>• Audit records</p></div></div>
        <div><div class="col-head">ClearSight QC™ Group</div><div class="small col-body"><p>Compares results across many plants.</p><p>• Central database</p><p>• Plant ranking</p><p>• Remote access</p></div></div>
      </div>
    </article>
    <article class="page">
      <svg style="position:absolute;left:0;top:0" width="520" height="140" aria-hidden="true">
        <path d="M0 30Q200 0 360 0H520V70Q250 70 0 140Z" fill="var(--green)"/>
      </svg>
      <div class="h-green abs" style="left:30px;top:26px;font-size:13px;line-height:1.2">Proving Solutions /<br>ROI Justification Example:<br>SEAMview RX Case Study</div>
      <div class="ph" role="img" aria-label="SEAMview RX bench unit" style="left:330px;top:80px;width:170px;height:110px;background:linear-gradient(160deg,#efefec,#c9cac6)"></div>
      <div class="abs" style="left:30px;top:210px;width:460px;display:grid;grid-template-columns:repeat(3,1fr);gap:10px">
        <div><div class="col-head">Case Study 1:<br>Cost Savings</div><div class="small col-body"><p>Less scrap and fewer manual tests saved one filler a full shift of lab work each week.</p><p>• Scrap cut by half</p><p>• Payback in one year</p></div></div>
        <div><div class="col-head">Case Study 2:<br>Time Savings</div><div class="small col-body"><p>Checks ran in a fraction of the usual time per can, freeing staff for other tests.</p><p>• 5× faster checks</p><p>• More cans sampled</p></div></div>
        <div><div class="col-head">Service and<br>Support</div><div class="small col-body"><p>Local teams keep every unit running, with spare parts and remote help worldwide.</p><p>• Yearly service plans</p><p>• Online support</p></div></div>
      </div>
      <div class="abs" style="left:0;top:440px;width:520px;height:296px;background:var(--green)">
        <div class="ph" role="img" aria-label="World map showing service locations" style="left:40px;top:30px;width:440px;height:230px;background:radial-gradient(ellipse at center,#1a9a6c,#00845a 70%)"></div>
      </div>
    </article>
  </div>
</section>

</body>
</html>
```